Satin Decor Paint Label

We will have three different sizes for this label but the dimensions for the medium size are 2" tall by 11.75'' wide. Please work off that.

Our colors are typically black and white but feel free to incorporate silver, gold, bronze or any combination. We would like to see multiple color variations of your designs.

General Info needed on label:
4627
Coatings
Interior Decor Paint
Furniture, Trim, Cabinets
Acrylic Waterborne Urethane
Satin Finish
16 FL. OZ. - 473 mL
````````````````````````````````````````````````````````````````````````````````````````````
Your design does not have to be the same as the one in the attached image.

You can put Satin Finish or Interior Decor Paint or something else going vertically up the side.

The label will be on a container like the the one in the attached image. Please have your design work on the same container.

```html
<!DOCTYPE html>
<html lang="en">
<head>
<meta charset="utf-8">
<title>4627 Coatings – Satin Decor Paint Label Options</title>
<link rel="stylesheet" href="https://fonts.googleapis.com/css2?family=Oswald:wght@600&family=Montserrat:wght@500;600&family=Archivo+Black&display=swap">
<style>
  :root {
    --backdrop: #dedede;
    --ink: #0c0c0c;
    --label-black: #111111;
    --white: #ffffff;
  }
  * { margin: 0; padding: 0; box-sizing: border-box; }
  html, body {
    width: 1200px;
    height: 938px;
    overflow: hidden;
    background: var(--backdrop);
  }
  .board {
    position: relative;
    width: 1200px;
    height: 938px;
  }
  .option {
    position: absolute;
    top: 140px;
    width: 460px;
    text-align: center;
  }
  .option--one { left: 110px; }
  .option--two { left: 630px; }
  .option-title {
    font-family: "Montserrat", sans-serif;
    font-weight: 500;
    font-size: 36px;
    color: var(--ink);
    letter-spacing: 1px;
    margin-bottom: 110px;
  }
  .label {
    display: block;
    width: 460px;
    height: 360px;
  }
  .brand-name {
    font-family: "Montserrat", sans-serif;
    font-weight: 600;
    fill: var(--ink);
  }
  .product-name {
    font-family: "Oswald", sans-serif;
    font-weight: 600;
    fill: var(--ink);
  }
  .uses {
    font-family: "Montserrat", sans-serif;
    font-weight: 600;
    fill: var(--ink);
  }
  .formula,
  .volume {
    font-family: "Montserrat", sans-serif;
    font-weight: 600;
    fill: var(--white);
  }
  .finish {
    font-family: "Archivo Black", sans-serif;
    fill: #2a2a2c;
    stroke: #d8d8dc;
    stroke-width: 1.6;
    paint-order: stroke;
  }
</style>
</head>
<body>
<main class="board">

  <section class="option option--one">
    <h2 class="option-title">OPTION 1</h2>
    <svg class="label" viewBox="0 0 460 360" xmlns="http://www.w3.org/2000/svg">
      <defs>
        <linearGradient id="silver-satin" x1="0" y1="0" x2="1" y2="1">
          <stop offset="0" stop-color="#b4b4b9"/>
          <stop offset="0.5" stop-color="#a5a5aa"/>
          <stop offset="1" stop-color="#9c9ca1"/>
        </linearGradient>
        <linearGradient id="gold-one" x1="0" y1="0" x2="1" y2="0">
          <stop offset="0" stop-color="#b8892a"/>
          <stop offset="0.35" stop-color="#ecd27a"/>
          <stop offset="0.7" stop-color="#c9a23a"/>
          <stop offset="1" stop-color="#8c8c90"/>
        </linearGradient>
      </defs>
      <rect width="460" height="360" fill="url(#silver-satin)"/>
      <path d="M0,188 Q230,390 460,200 L460,360 L0,360 Z" fill="var(--label-black)"/>
      <path d="M0,176 Q230,378 460,188" fill="none" stroke="url(#gold-one)" stroke-width="3.5"/>
      <text class="brand-name" x="205" y="122" font-size="68" text-anchor="middle">4627</text>
      <text class="brand-name" x="205" y="158" font-size="20" letter-spacing="3" text-anchor="middle">COATINGS</text>
      <rect x="88" y="186" width="250" height="40" fill="none" stroke="url(#gold-one)" stroke-width="1.5"/>
      <text class="product-name" x="213" y="217" font-size="25" text-anchor="middle">INTERIOR DECOR PAINT</text>
      <text class="uses" x="213" y="250" font-size="12.5" text-anchor="middle">FURNITURE, TRIM, CABINETS</text>
      <text class="formula" x="213" y="313" font-size="8.5" letter-spacing="0.6" text-anchor="middle">ACRYLIC WATERBORNE URETHANE</text>
      <rect x="160" y="328" width="106" height="16" rx="8" fill="none" stroke="url(#gold-one)" stroke-width="1.8"/>
      <text class="volume" x="213" y="339.5" font-size="7.5" text-anchor="middle">16 FL. OZ. - 473 mL</text>
      <text class="finish" transform="translate(425 178) rotate(-90)" font-size="34" text-anchor="middle">SATIN FINISH</text>
    </svg>
  </section>

  <section class="option option--two">
    <h2 class="option-title">OPTION 2</h2>
    <svg class="label" viewBox="0 0 460 360" xmlns="http://www.w3.org/2000/svg">
      <defs>
        <linearGradient id="silver-chrome" x1="0" y1="0" x2="1" y2="0">
          <stop offset="0" stop-color="#86868c"/>
          <stop offset="0.1" stop-color="#d4d4d8"/>
          <stop offset="0.25" stop-color="#a4a4aa"/>
          <stop offset="0.45" stop-color="#e8e8ec"/>
          <stop offset="0.6" stop-color="#b4b4ba"/>
          <stop offset="0.75" stop-color="#d6d6da"/>
          <stop offset="0.9" stop-color="#8c8c92"/>
          <stop offset="1" stop-color="#7a7a80"/>
        </linearGradient>
        <linearGradient id="gold-two" x1="0" y1="0" x2="1" y2="0">
          <stop offset="0" stop-color="#b8892a"/>
          <stop offset="0.35" stop-color="#f0da86"/>
          <stop offset="0.7" stop-color="#c9a23a"/>
          <stop offset="1" stop-color="#a0a0a4"/>
        </linearGradient>
      </defs>
      <rect width="460" height="360" fill="url(#silver-chrome)"/>
      <path d="M0,188 Q230,390 460,200 L460,360 L0,360 Z" fill="var(--label-black)"/>
      <path d="M0,176 Q230,378 460,188" fill="none" stroke="url(#gold-two)" stroke-width="3.5"/>
      <text class="brand-name" x="205" y="122" font-size="68" text-anchor="middle">4627</text>
      <text class="brand-name" x="205" y="158" font-size="20" letter-spacing="3" text-anchor="middle">COATINGS</text>
      <rect x="88" y="186" width="250" height="40" fill="none" stroke="url(#gold-two)" stroke-width="1.5"/>
      <text class="product-name" x="213" y="217" font-size="25" text-anchor="middle">INTERIOR DECOR PAINT</text>
      <text class="uses" x="213" y="250" font-size="12.5" text-anchor="middle">FURNITURE, TRIM, CABINETS</text>
      <text class="formula" x="213" y="313" font-size="8.5" letter-spacing="0.6" text-anchor="middle">ACRYLIC WATERBORNE URETHANE</text>
      <rect x="160" y="328" width="106" height="16" rx="8" fill="none" stroke="url(#gold-two)" stroke-width="1.8"/>
      <text class="volume" x="213" y="339.5" font-size="7.5" text-anchor="middle">16 FL. OZ. - 473 mL</text>
      <text class="finish" transform="translate(425 178) rotate(-90)" font-size="34" text-anchor="middle">SATIN FINISH</text>
    </svg>
  </section>

</main>
</body>
</html>
```